"Stovelight" album cover and promo art

I'm working on an album and am looking for a graphic to be created that I can use as an overlay on the album cover as well as other elements of the campaign. I'm looking to be able to use the same graphic/ logo on t-shirts, social media pages, and print materials if needed. Below is some info I hope will be helpful.
Artist: Dorian Velsh'
Genre: Hip-Hop/Rap - positive
Album Name: STOVELIGHT
Background: California native. This album is representing coming back home to CA and reflects some of the stories and influence in my life. Goal of my music is to bring people up, not down, and promote a positive and inspirational alternative to other music out.
Art Concept: I envision the State of California built by different language versions of the word
"
Home". I'd like to have the English to be the biggest most visible, with other languages spoken of the world, like Spanish, French, Japanese, Mandrin, Hebrew, Arabic, etc. so the actual words would form the State outline.
Also looking for the word STOVELIGHT at the bottom of the graphic(maybe in a font that looks like bandana print). Ideally I'd like the ability to adjust transparency as I'll use different images/pics of CA behind it for different options as well as photos from an upcoming photo shoot. I'd also like to use it for t-shirts, flyers, etc.
Market: Ideal group should resonate with 15-35. Will most definetley resonate with native Californian's and others who have lived or love to visit the area.
Hopefully this is helpful context for the project.

```html
<!DOCTYPE html>
<html lang="en">
<head>
<meta charset="utf-8">
<title>Dorian Velsh – Stovelight</title>
<link rel="stylesheet" href="https://fonts.googleapis.com/css2?family=Oswald:wght@400&family=Yellowtail&display=swap">
<style>
  :root {
    --gap-white: #f1eef0;
    --stripe-peach: #e9a27c;
    --stripe-orange: #eb8552;
    --stripe-coral: #dc4058;
    --stripe-rose: #d4465a;
    --stripe-mauve: #c84a7f;
    --stripe-magenta: #d93fb3;
    --artist-lilac: #e8a3e4;
    --title-white: #f7f5f6;
  }
  html, body {
    margin: 0;
    padding: 0;
    width: 1200px;
    height: 1114px;
    overflow: hidden;
    background: var(--gap-white);
  }
  .album-cover {
    position: relative;
    width: 1200px;
    height: 1114px;
    overflow: hidden;
  }
  .cover-art {
    position: absolute;
    inset: 0;
    display: block;
  }
  .artist-name {
    position: absolute;
    left: 0;
    right: 0;
    top: 768px;
    margin: 0 0 0 34px;
    text-align: center;
    font-family: "Oswald", "Arial Narrow", sans-serif;
    font-weight: 400;
    font-size: 58px;
    letter-spacing: 5px;
    color: var(--artist-lilac);
    line-height: 1;
  }
  .album-title {
    position: absolute;
    left: 0;
    right: 0;
    top: 838px;
    margin: 0 0 0 8px;
    text-align: center;
    font-family: "Yellowtail", cursive;
    font-weight: 400;
    font-size: 188px;
    color: var(--title-white);
    line-height: 1;
  }
</style>
</head>
<body>
<main class="album-cover">
  <svg class="cover-art" width="1200" height="1114" viewBox="0 0 1200 1114" role="img"
       aria-label="Beach photo at dusk seen through tinted vertical colour bands: a lifeguard tower, a couple sitting on the sand, a woman walking and seagulls in the sky">
    <defs>
      <linearGradient id="sand-shade" x1="0" y1="0" x2="0" y2="1">
        <stop offset="0" stop-color="#2a1830" stop-opacity="0.55"/>
        <stop offset="1" stop-color="#1c1020" stop-opacity="0.7"/>
      </linearGradient>
    </defs>
    <rect class="band-gap" x="0" y="0" width="1200" height="1114" fill="var(--gap-white)"/>
    <rect class="band" x="0" y="0" width="153" height="1114" fill="var(--stripe-peach)"/>
    <rect class="band" x="172" y="0" width="166" height="1114" fill="var(--stripe-orange)"/>
    <rect class="band" x="356" y="0" width="237" height="1114" fill="var(--stripe-coral)"/>
    <rect class="band" x="612" y="0" width="237" height="1114" fill="var(--stripe-rose)"/>
    <rect class="band" x="868" y="0" width="165" height="1114" fill="var(--stripe-mauve)"/>
    <rect class="band" x="1052" y="0" width="148" height="1114" fill="var(--stripe-magenta)"/>
    <polygon class="beach-sand" points="0,600 300,596 600,594 900,598 1200,610 1200,1114 0,1114"
             fill="url(#sand-shade)"/>
    <polygon class="beach-sand-left" points="0,600 172,599 172,1114 0,1114" fill="#4a4a4a" opacity="0.85"/>
  </svg>
  <p class="artist-name">- DORIAN VELSH -</p>
  <h1 class="album-title">Stovelight</h1>
</main>
</body>
</html>
```